Crowler Can Design

Looking for a design for a crowler can we are going to be adding to our restaurant sales fleet. Would like it to be a cool design, that fits our brand. I have attached the artwork file specifications that need to be followed, I have also attached some different logos/marks for the brand - in addition to the crowler logo we would like to have prominently displayed on the can.

```html
<!DOCTYPE html>
<html lang="en">
<head>
<meta charset="utf-8">
<title>Prairie Alehouse Crowler Label</title>
<link rel="stylesheet" href="https://fonts.googleapis.com/css2?family=Oswald:wght@500;700&family=Libre+Baskerville:wght@400&display=swap">
<style>
  :root {
    --page: #dfe5e5;
    --silver-light: #f4f5f6;
    --silver-mid: #d9dcdf;
    --silver-dark: #b9bec3;
    --ink: #1c1c1c;
    --strip: #2b2b2b;
    --strip-text: #e6e6e6;
    --info-box: #f1e6ec;
    --info-border: #cfd2d4;
    --band: #f7f7f7;
    --ring-tone: #c4c8cc;
  }
  * { box-sizing: border-box; margin: 0; padding: 0; }
  html, body { width: 1200px; height: 1200px; overflow: hidden; }
  body {
    background: var(--page);
    display: flex;
    align-items: center;
    justify-content: center;
    font-family: "Oswald", sans-serif;
    color: var(--ink);
  }
  .label-wrap {
    position: relative;
    width: 1100px;
    height: 640px;
    overflow: hidden;
    background: linear-gradient(90deg, var(--silver-mid) 0%, var(--silver-light) 18%, var(--silver-mid) 34%, var(--silver-light) 50%, var(--silver-mid) 66%, var(--silver-light) 82%, var(--silver-mid) 100%);
    box-shadow: 0 10px 30px rgba(0,0,0,0.12);
  }
  .ring-pattern {
    position: absolute;
    border-radius: 50%;
    background: radial-gradient(circle, rgba(255,255,255,0.0) 0%, rgba(196,200,204,0.35) 55%, rgba(196,200,204,0.55) 70%, rgba(255,255,255,0) 71%);
  }
  .ring-pattern--center { width: 520px; height: 520px; left: 290px; top: 20px; }
  .ring-pattern--side { width: 380px; height: 380px; left: 150px; top: 110px; }

  /* Left panel */
  .legal-strip {
    position: absolute;
    left: 40px; top: 30px;
    width: 110px; height: 520px;
    background: var(--strip);
    color: var(--strip-text);
  }
  .recycle-mark {
    position: absolute;
    left: 33px; top: 24px;
    width: 44px; height: 44px;
    border: 2px solid var(--strip-text);
  }
  .recycle-caption {
    position: absolute;
    top: 76px; width: 100%;
    text-align: center;
    font-family: "Libre Baskerville", serif;
    font-size: 10px;
    letter-spacing: 1px;
  }
  .legal-text {
    position: absolute;
    left: 55px; top: 320px;
    width: 380px;
    transform: translate(-50%, -50%) rotate(-90deg);
    font-size: 9px;
    line-height: 1.45;
    letter-spacing: 0.6px;
    text-transform: uppercase;
  }
  .social-row {
    position: absolute;
    left: 170px; top: 470px;
    transform-origin: left top;
    transform: rotate(-90deg);
    display: flex;
    align-items: center;
    gap: 10px;
    font-size: 15px;
    font-weight: 700;
    letter-spacing: 0.5px;
    white-space: nowrap;
  }
  .social-dot {
    width: 22px; height: 22px;
    border: 2px solid var(--ink);
    border-radius: 50%;
  }
  .social-slash { font-size: 22px; font-weight: 500; }

  /* Center panel */
  .brand-lockup {
    position: absolute;
    left: 350px; top: 150px;
    width: 400px;
    text-align: center;
  }
  .brand-disc {
    width: 150px; height: 150px;
    margin: 0 auto 18px;
    border-radius: 50%;
    background: var(--ink);
  }
  .brand-name {
    font-size: 62px;
    font-weight: 700;
    line-height: 1;
    letter-spacing: 1px;
  }
  .brand-sub {
    margin-top: 8px;
    display: flex;
    align-items: center;
    justify-content: center;
    gap: 10px;
    font-size: 19px;
    font-weight: 700;
    letter-spacing: 2px;
  }
  .brand-sub::before, .brand-sub::after {
    content: "";
    width: 60px; height: 3px;
    background: var(--ink);
  }

  /* Right panel */
  .batch-box {
    position: absolute;
    left: 840px; top: 40px;
    width: 220px; height: 330px;
    background: var(--info-box);
    border: 2px solid var(--info-border);
    display: flex;
    flex-direction: column;
    justify-content: space-around;
    align-items: center;
    padding: 16px 0;
    font-family: "Libre Baskerville", serif;
    font-size: 14px;
    font-weight: 400;
  }
  .brand-story {
    position: absolute;
    left: 810px; top: 395px;
    width: 270px;
    text-align: center;
    font-family: "Libre Baskerville", serif;
    font-size: 16px;
    line-height: 1.4;
  }

  /* Bottom band */
  .tagline-band {
    position: absolute;
    left: 0; bottom: 40px;
    width: 100%; height: 40px;
    background: var(--band);
    display: flex;
    align-items: center;
    overflow: hidden;
    white-space: nowrap;
    font-size: 20px;
    font-weight: 700;
    letter-spacing: 1px;
  }
  .tagline-band span { padding: 0 14px; }
  .label-foot {
    position: absolute;
    left: 0; bottom: 0;
    width: 100%; height: 40px;
    background: linear-gradient(90deg, var(--silver-dark), var(--silver-light), var(--silver-dark), var(--silver-light), var(--silver-dark));
  }
</style>
</head>
<body>
  <main class="label-wrap">
    <div class="ring-pattern ring-pattern--side" role="img" aria-label="Concentric line pattern"></div>
    <div class="ring-pattern ring-pattern--center" role="img" aria-label="Concentric line pattern behind the brand mark"></div>

    <section class="legal-strip">
      <div class="recycle-mark"></div>
      <div class="recycle-caption">RECYCLE</div>
      <p class="legal-text">Government warning: (1) According to the Surgeon General, women should not drink alcoholic beverages during pregnancy because of the risk of birth defects. (2) Consumption of alcoholic beverages impairs your ability to drive a car or operate machinery, and may cause health problems.</p>
    </section>

    <div class="social-row">
      <span class="social-dot"></span>
      <span class="social-dot"></span>
      <span class="social-dot"></span>
      <span class="social-slash">/</span>
      <span>PRAIRIE ALEHOUSE</span>
    </div>

    <section class="brand-lockup">
      <div class="brand-disc"></div>
      <div class="brand-name">PRAIRIE</div>
      <div class="brand-sub">ALEHOUSE</div>
    </section>

    <section class="batch-box">
      <span>NAME</span>
      <span>STYLE</span>
      <span>ALC/VOL</span>
      <span>DATE</span>
    </section>

    <p class="brand-story">At Fieldline, we believe in making things right. We strive to make the best possible for you and your friends. We also work hard to help others make things right.</p>

    <div class="tagline-band">
      <span>CRAFT BEER</span><span>+</span><span>CRAFT BEEF</span><span>+</span>
      <span>CRAFT BEER</span><span>+</span><span>CRAFT BEEF</span><span>+</span>
      <span>CRAFT BEER</span><span>+</span><span>CRAFT BEEF</span><span>+</span>
      <span>CRAFT BEER</span><span>+</span><span>CRAFT BEEF</span><span>+</span>
      <span>CRAFT BEER</span>
    </div>
    <div class="label-foot"></div>
  </main>
</body>
</html>
```